Outdoor kitchen and Appliance Need new business card

We need a new business card, for our business.

Front side with all info, back side with more brand identity.

I have attached some drafts, we moved up but it lacks creativity.

Use https://photos.quendrix.com and I can purchase, the stock photo and send it you if you design is chosen.

We are also planing on printing business card with the logo, having a spot uv. I have attached instructions.

Plumtarvessa.com is our website

Target Market(s)

Extremely high end customer.

Contact Information for Business Card

Double sided with spot uv on logos

Colors
ec1f27

Requirements
Must have
• See sample I have attached, we are open to ideas.

Colors, are: RED, Stainless steel, Black

```html
<!DOCTYPE html>
<html lang="en">
<head>
<meta charset="utf-8">
<title>Plumtarvessa Business Card</title>
<link href="https://fonts.googleapis.com/css2?family=Open+Sans:wght@400;700&display=swap" rel="stylesheet">
<style>
  :root {
    --backdrop: #c9c9c9;
    --card-black: #1c1c1c;
    --card-sheen: #3a3a3a;
    --steel: #b9b9b9;
    --steel-light: #e2e2e2;
    --rule: #8a8a8a;
    --brand-red: #ec1f27;
    --white: #ffffff;
  }
  * { margin: 0; padding: 0; box-sizing: border-box; }
  html, body {
    width: 1200px; height: 675px; overflow: hidden;
    background: var(--backdrop);
    font-family: "Open Sans", Arial, sans-serif;
  }
  .sheet {
    position: relative; width: 1200px; height: 675px;
    display: flex; align-items: center; justify-content: center; gap: 60px;
  }
  .card {
    position: relative; width: 510px; height: 292px;
    border-radius: 14px; overflow: hidden;
    background: linear-gradient(115deg, var(--card-black) 0%, var(--card-sheen) 45%, var(--card-black) 70%, #151515 100%);
    box-shadow: 0 14px 30px rgba(0,0,0,.28);
  }
  .brand {
    position: absolute; display: flex; align-items: center; gap: 12px;
    color: var(--steel); font-weight: 700; letter-spacing: 3px; white-space: nowrap;
  }
  .brand-dot {
    width: 20px; height: 20px; border-radius: 50%; background: var(--brand-red); flex: none;
  }
  .card-back .brand {
    left: 50%; top: 50%; transform: translate(-50%, -50%);
    font-size: 34px;
  }
  .card-front .brand {
    left: 38px; top: 54px; font-size: 24px;
  }
  .card-front .brand-dot { width: 16px; height: 16px; }
  .info {
    position: absolute; left: 150px; width: 220px; top: 124px;
    border-top: 1px solid var(--rule); border-bottom: 1px solid var(--rule);
    padding: 9px 0 8px;
  }
  .contact-row {
    display: flex; align-items: center; gap: 9px;
    color: var(--steel-light); font-size: 10.5px; line-height: 19px; white-space: nowrap;
  }
  .contact-row.continued { padding-left: 21px; }
  .contact-row svg { width: 12px; height: 12px; flex: none; }
  .social {
    display: flex; justify-content: flex-end; gap: 6px; margin-top: 6px;
  }
  .social span {
    width: 13px; height: 13px; border-radius: 3px; background: var(--steel);
  }
  .person {
    position: absolute; right: 32px; top: 150px; text-align: right; color: var(--white);
  }
  .person-name { font-size: 22px; font-weight: 700; letter-spacing: 1px; line-height: 1; }
  .person-role { font-size: 10px; color: var(--steel); margin-top: 4px; }
</style>
</head>
<body>
<main class="sheet">
  <section class="card card-back" aria-label="Card back">
    <div class="brand"><span class="brand-dot"></span>PLUMTARVESSA</div>
  </section>

  <section class="card card-front" aria-label="Card front">
    <div class="brand"><span class="brand-dot"></span>PLUMTARVESSA</div>

    <div class="info">
      <div class="contact-row">
        <svg viewBox="0 0 12 12"><path d="M6 1a3.5 3.5 0 0 0-3.5 3.5C2.5 7.5 6 11 6 11s3.5-3.5 3.5-6.5A3.5 3.5 0 0 0 6 1zm0 5a1.5 1.5 0 1 1 0-3 1.5 1.5 0 0 1 0 3z" fill="#ec1f27"/></svg>
        <span>418 Alder Grove Way Ste 4</span>
      </div>
      <div class="contact-row continued"><span>Marlow Bay, FL 30912</span></div>
      <div class="contact-row">
        <svg viewBox="0 0 12 12"><path d="M3 1.5l2 2-1 1.2a6 6 0 0 0 3.3 3.3l1.2-1 2 2-1.2 1.5C5.5 10.3 1.7 6.5 1.5 2.7z" fill="#ec1f27"/></svg>
        <span>(555)014-2273</span>
      </div>
      <div class="contact-row">
        <svg viewBox="0 0 12 12"><rect x="1" y="2.5" width="10" height="7" rx="1" fill="none" stroke="#ec1f27"/><path d="M1.5 3l4.5 3.5L10.5 3" fill="none" stroke="#ec1f27"/></svg>
        <span>Sales@plumtarvessa.com</span>
      </div>
      <div class="contact-row">
        <svg viewBox="0 0 12 12"><circle cx="6" cy="6" r="4.8" fill="none" stroke="#ec1f27"/><ellipse cx="6" cy="6" rx="2" ry="4.8" fill="none" stroke="#ec1f27"/><path d="M1.2 6h9.6" stroke="#ec1f27"/></svg>
        <span>www.plumtarvessa.com</span>
      </div>
      <div class="social" aria-hidden="true"><span></span><span></span></div>
    </div>

    <div class="person">
      <div class="person-name">NAME</div>
      <div class="person-role">Owner</div>
    </div>
  </section>
</main>
</body>
</html>
```